Brochure & Business card design

Looking for a new business card design i want it to be modern and sharp looking i usually order plastic business cards, and i would like to make the colors like the logo teal/charcoal i will like to have our services on icons with words.... our services are
ROOFING GUTTERS PAINTING PRESSURE WASHING EXTERIOR DESIGN & ATTIC VENTILATION. I also want to add my credentials

Target Market(s)

Oregon local market

Industry/Entity Type

Residential Construction

Contact Information for Business Card

Business info, services, number, website

Font styles to use
Serif
Sans Serif

Colors
33b8a4
5c5c5c
ffffff

Requirements
Must have
• Dale Finch
• Cell:
• Office:
• Email:
• Website:
• also i need our social media icons
• Services ROOFING GUTTERS PAINTING PRESSURE WASHING EXTERIOR DESIGN & ATTIC VENTILATION
• -icons for number, web, email, cell
• OR #584312
• Wa #KTRABLD461X7
Nice to have
• -Clean design Front & Back
• -Icons
• -shape House just like logo design
• -First Impression
Should not have
• Not Busy or lost of eye contact

```html
<!DOCTYPE html>
<html lang="en">
<head>
<meta charset="utf-8">
<title>Ridgeline Exteriors – Business Card</title>
<link rel="stylesheet" href="https://fonts.googleapis.com/css2?family=Roboto:wght@400;500;700&family=Tinos:wght@400;700&display=swap">
<style>
  :root {
    --teal: #17877a;
    --charcoal: #4a4a4a;
    --ink: #3d3d3d;
    --card: #f7f8f8;
    --page: #e4e7ea;
    --white: #ffffff;
  }
  * { margin: 0; padding: 0; box-sizing: border-box; }
  html, body { width: 1200px; height: 900px; overflow: hidden; }
  body { background: var(--page); font-family: "Roboto", Arial, sans-serif; position: relative; }

  .card {
    position: absolute; left: 120px; top: 177px;
    width: 960px; height: 546px;
    background: var(--card);
    border-radius: 22px;
    box-shadow: 0 10px 30px rgba(0,0,0,0.12);
  }

  .holder { position: absolute; left: 58px; top: 52px; }
  .holder-name {
    font-family: "Tinos", "Times New Roman", serif; font-weight: 700;
    font-size: 44px; letter-spacing: 1px; color: var(--ink); line-height: 1;
  }
  .holder-role {
    font-family: "Tinos", "Times New Roman", serif;
    font-size: 25px; color: var(--teal); margin-top: 6px;
  }

  .contact-list { position: absolute; left: 58px; top: 158px; list-style: none; }
  .contact-item { display: flex; align-items: center; height: 38.5px; font-size: 25px; color: var(--ink); }
  .contact-icon {
    width: 30px; height: 30px; background: var(--teal); margin-right: 16px;
    display: flex; align-items: center; justify-content: center; flex: none;
  }

  .social-list { position: absolute; left: 58px; top: 370px; display: flex; gap: 5px; }
  .social-square { width: 31px; height: 31px; background: var(--teal); }

  .brand {
    position: absolute; left: 600px; top: 120px; width: 320px;
    display: flex; align-items: center; justify-content: center; gap: 14px;
  }
  .brand-mark { width: 26px; height: 26px; background: var(--teal); flex: none; }
  .brand-name {
    font-family: "Roboto", Arial, sans-serif; font-weight: 700; color: var(--teal);
    font-size: 36px; line-height: 1.15; letter-spacing: 1px;
  }

  .credentials { position: absolute; left: 615px; top: 353px; display: flex; gap: 20px; }
  .badge-plain { height: 48px; border-radius: 6px; }
  .badge-a { width: 142px; background: #7d7d7d; }
  .badge-b { width: 126px; background: var(--charcoal); }

  .divider { position: absolute; left: 58px; top: 424px; width: 847px; height: 4px; display: flex; }
  .divider-teal { width: 430px; background: var(--teal); }
  .divider-charcoal { flex: 1; background: var(--charcoal); }

  .services { position: absolute; left: 0; width: 960px; display: flex; justify-content: center; align-items: center; }
  .services-row-1 { top: 450px; }
  .services-row-2 { top: 493px; }
  .service { display: flex; align-items: center; font-size: 22px; color: var(--charcoal); letter-spacing: 0.3px; }
  .service svg { margin-right: 12px; }
  .sep { color: #888; margin: 0 16px; font-size: 18px; }
</style>
</head>
<body>
  <div class="card">
    <div class="holder">
      <div class="holder-name">DALE FINCH</div>
      <div class="holder-role">Managing Director</div>
    </div>

    <ul class="contact-list">
      <li class="contact-item">
        <span class="contact-icon"><svg width="14" height="20" viewBox="0 0 14 20"><rect x="1" y="1" width="12" height="18" rx="2" fill="none" stroke="#fff" stroke-width="2"/><circle cx="7" cy="15.5" r="1.3" fill="#fff"/></svg></span>
        073-418-205-619
      </li>
      <li class="contact-item">
        <span class="contact-icon"><svg width="18" height="18" viewBox="0 0 24 24"><path fill="#fff" d="M6.6 10.8a15.1 15.1 0 006.6 6.6l2.2-2.2c.3-.3.7-.4 1-.2 1.1.4 2.3.6 3.6.6.6 0 1 .4 1 1V20c0 .6-.4 1-1 1A17 17 0 013 4c0-.6.4-1 1-1h3.5c.6 0 1 .4 1 1 0 1.3.2 2.5.6 3.6.1.3 0 .7-.2 1z"/></svg></span>
        052-617-348-901
      </li>
      <li class="contact-item">
        <span class="contact-icon"><svg width="18" height="14" viewBox="0 0 18 14"><rect x="1" y="1" width="16" height="12" fill="none" stroke="#fff" stroke-width="1.6"/><path d="M1 1l8 7 8-7" fill="none" stroke="#fff" stroke-width="1.6"/></svg></span>
        dalefinch@ridgelinexteriors.com
      </li>
      <li class="contact-item">
        <span class="contact-icon"><svg width="18" height="18" viewBox="0 0 20 20"><g fill="none" stroke="#fff" stroke-width="1.4"><circle cx="10" cy="10" r="8.5"/><ellipse cx="10" cy="10" rx="3.8" ry="8.5"/><path d="M1.5 10h17M3 5.5h14M3 14.5h14"/></g></svg></span>
        www.ridgelinexteriors.com
      </li>
    </ul>

    <div class="social-list">
      <span class="social-square"></span>
      <span class="social-square"></span>
      <span class="social-square"></span>
      <span class="social-square"></span>
    </div>

    <div class="brand">
      <span class="brand-mark"></span>
      <div class="brand-name">RIDGELINE<br>EXTERIORS</div>
    </div>

    <div class="credentials">
      <span class="badge-plain badge-a"></span>
      <span class="badge-plain badge-b"></span>
    </div>

    <div class="divider"><span class="divider-teal"></span><span class="divider-charcoal"></span></div>

    <div class="services services-row-1">
      <span class="service"><svg width="26" height="22" viewBox="0 0 26 22"><path d="M2 20L16 6M5 20l14-14" stroke="var(--teal)" stroke-width="3" fill="none"/><path d="M14 2l8 8" stroke="var(--teal)" stroke-width="3"/></svg>ROOFING</span>
      <span class="sep">|</span>
      <span class="service"><svg width="24" height="20" viewBox="0 0 24 20"><path d="M1 2h22v6H14v11H9V8H1z" fill="var(--teal)"/></svg>GUTTERS</span>
      <span class="sep">|</span>
      <span class="service"><svg width="22" height="22" viewBox="0 0 22 22"><path d="M20 2l-9 9" stroke="var(--teal)" stroke-width="4"/><path d="M9 11l-6 6 2 3 6-6z" fill="var(--teal)"/></svg>PAINTING</span>
      <span class="sep">|</span>
      <span class="service"><svg width="26" height="22" viewBox="0 0 26 22"><path d="M4 18h10l4-6H8z" fill="var(--teal)"/><path d="M18 10l6-6M20 14l5-2M16 8l2-6" stroke="var(--teal)" stroke-width="2"/></svg>PRESSURE WASHING</span>
    </div>

    <div class="services services-row-2">
      <span class="service"><svg width="22" height="22" viewBox="0 0 22 22"><rect x="2" y="6" width="18" height="15" fill="var(--teal)"/><g fill="#fff"><rect x="5" y="9" width="3" height="3"/><rect x="10" y="9" width="3" height="3"/><rect x="15" y="9" width="3" height="3"/><rect x="5" y="14" width="3" height="3"/><rect x="15" y="14" width="3" height="3"/></g><rect x="6" y="2" width="10" height="4" fill="var(--teal)"/></svg>EXTERIOR DESIGN</span>
      <span class="sep">|</span>
      <span class="service"><svg width="24" height="22" viewBox="0 0 24 22"><g stroke="var(--teal)" stroke-width="2.4" fill="none"><path d="M4 20V6M12 20V6M20 20V6"/><path d="M1 9l3-4 3 4M9 9l3-4 3 4M17 9l3-4 3 4"/></g></svg>ATTIC VENTILATION</span>
    </div>
  </div>
</body>
</html>
```